BrisaLume Supplement Bottle Label

We need our label redesigned with a fresh spin! :)

I really like bright colors, bright blue, and bright green are the two colors I'd like to use, but want a CLEAN PROFESSIONAL MEDICAL feel overall. Think Zelvan

I see myself as a bridge between science-based medicine and natural medicine and that is also my wish for Brisalume, my supplement brand.

I like the root in the background of the bottle

I also like the new BL symbols below

I am also attaching my book image. I'd like the Brisalume brand to complement my Quiet Current brand :-)
Updates

Project Deadline Extended Reason: We are now guaranteeing the payment to get a design we like :) Added Thursday, May 19, 2016

Still looking for a clean, modern, professional, medical feel :) Added Thursday, May 19, 2016

Industry/Entity Type

Health And Wellness

Font styles to use
Serif
Sans Serif

Requirements
Must have
• Blue- for medical
• Green- for natural
• The word Brisa should be in green, Blue- should be for -Lume.
Nice to have
• I'd like the product labels to convey the brand: vibrant, health restoring, trustworthy, professional. The colorful one we looked at was one I really liked.

```html
<!DOCTYPE html>
<html lang="en">
<head>
<meta charset="utf-8">
<title>BrisaLume Pea Protein Label</title>
<link href="https://fonts.googleapis.com/css2?family=Lato:wght@300;400&display=swap" rel="stylesheet">
<style>
  :root {
    --canvas: #f4f6f6;
    --label: #ffffff;
    --brand-green: #2f9a3f;
    --brand-blue: #1f5fa8;
    --band-teal: #1e6f86;
    --ink: #3e4446;
    --root-tone: #cfe3dc;
  }
  html, body {
    margin: 0;
    padding: 0;
    width: 1200px;
    height: 1200px;
    overflow: hidden;
    background: var(--canvas);
  }
  .label {
    position: absolute;
    left: 180px;
    top: 75px;
    width: 840px;
    height: 1050px;
    background: var(--label);
    overflow: hidden;
    font-family: "Lato", sans-serif;
    box-shadow: 0 0 0 1px #e3e8e8;
  }
  .root-artwork {
    position: absolute;
    left: 120px;
    top: 0;
    width: 720px;
    height: 1050px;
    background: radial-gradient(ellipse 60% 70% at 60% 45%, var(--root-tone) 0%, rgba(207,227,220,0.45) 55%, rgba(255,255,255,0) 100%);
  }
  .brand-mark {
    position: absolute;
    left: 11px;
    top: 109px;
    width: 146px;
    height: 146px;
    border: 3px solid var(--brand-green);
    border-radius: 50%;
    box-sizing: border-box;
    background: var(--label);
  }
  .brand-name {
    position: absolute;
    left: 73px;
    top: 640px;
    transform: translate(-50%, -50%) rotate(-90deg);
    font-weight: 300;
    font-size: 100px;
    line-height: 1;
    white-space: nowrap;
  }
  .brand-name-first { color: var(--brand-green); }
  .brand-name-second { color: var(--brand-blue); }
  .product-name {
    position: absolute;
    left: 238px;
    top: 688px;
    margin: 0;
    font-weight: 400;
    font-size: 104px;
    line-height: 1;
    color: var(--brand-green);
    white-space: nowrap;
  }
  .product-type {
    position: absolute;
    left: 235px;
    top: 812px;
    width: 600px;
    height: 98px;
    background: var(--band-teal);
    color: #ffffff;
    font-weight: 400;
    font-size: 52px;
    letter-spacing: 2px;
    line-height: 98px;
    text-align: center;
  }
  .net-weight {
    position: absolute;
    left: 238px;
    top: 928px;
    font-weight: 400;
    font-size: 46px;
    color: var(--ink);
    white-space: nowrap;
  }
</style>
</head>
<body>
  <div class="label">
    <div class="root-artwork" role="img" aria-label="Faint pale green illustration of spreading plant roots"></div>
    <div class="brand-mark"></div>
    <div class="brand-name"><span class="brand-name-first">Brisa</span><span class="brand-name-second">Lume</span></div>
    <h1 class="product-name">Pea Protein</h1>
    <div class="product-type">Dietary Supplement</div>
    <div class="net-weight">Net WT. 450 g (1 LB)</div>
  </div>
</body>
</html>
```